Infographics for Zelmora

Zelmora company specializes in providing services for the organization of low-budget crowdsourcing research.
Crowdsourcing research - the solution of the problem by lots of people on a competitive basis. Types of research will not be limited to the design competition, and will cover all areas of economic activity.

The site contains the following sections: directory of research, user communities, where they can organize the communication according to common interests, forum, news ticker.

The site will feature two groups of users:
1. Organizers of commercial research - the firm or individual businessmen
2. Researchers of commercial research. Moreover, the organizers can act as executors in the research organized by other users.

Motives Organizers of research:
1. Solving business problems quickly and inexpensively, and the variability of solutions.
2. The possibility of recruiting the best researchers.
3. Self-promotion (positioning your company as an innovative, using cutting-edge technology solutions).
4. Doing Business with the times.

The motives of researchers:
1. Earnings with their knowledge by participating in competitions and receive the prize fund.
2. Employability organized research (if the customer makes an offer the researcher).
3. Intelligent Leisure
4. Communication: forum, chat with the professionals of their field of study.

Required:
Graphically show the behavior of two groups of people based on their motives.
Schematically, the sheet should be divided into two parts - the left diagram of the model of the organizers, to the right - the researchers. The middle - it is desirable that part where the researchers will provide solutions to problems of the organizers - the scheme intersect each other graphically.
This work will be used for placement on the website of the company, as well as in printed promotional products.

Target Market(s)

Entrepreneurs, businesses as well as economically active population of Russia

Industry/Entity Type

Communication

Requirements
Must have
• The company's logo from the attached file.
All decals made with cursive. All decails are editable.
The source file in vector format EPS.
Nice to have
• The color scheme of the site will match the logo, so it is desirable that the figure used the same color as the logo: black, gray, green. In an attachment, "firm color" color settings in the CMYK.
Schemes must come from the top down, page orientation - portrait.
Should not have
• Do not use photos. Only pictures.

```html
<!DOCTYPE html>
<html lang="en">
<head>
<meta charset="utf-8">
<title>Zelmora — Motives of Organizers and Researchers</title>
<link rel="stylesheet" href="https://fonts.googleapis.com/css2?family=Open+Sans:ital,wght@0,300;0,400;0,600;1,400&display=swap">
<style>
  :root {
    --ink: #3d3d3d;
    --charcoal: #3a3a3a;
    --steel: #8e8e8e;
    --silver: #b9b9b9;
    --lime: #8dc63f;
    --lime-soft: #c6e09f;
    --lime-pale: #a9d46b;
    --paper: #ffffff;
  }
  html, body {
    margin: 0;
    padding: 0;
    width: 1200px;
    height: 2603px;
    overflow: hidden;
    background: var(--paper);
  }
  .sheet { display: block; width: 1200px; height: 2603px; }
  .brand-name {
    font-family: "Open Sans", sans-serif;
    font-weight: 300;
    font-size: 180px;
    fill: var(--ink);
  }
  .brand-dot { fill: var(--lime); }
  .group-bar--organizers { fill: var(--steel); }
  .group-bar--researchers { fill: var(--lime-soft); }
  .group-label {
    font-family: "Open Sans", sans-serif;
    font-style: italic;
    font-size: 34px;
    fill: var(--paper);
    text-anchor: middle;
  }
  .figure--organizers { fill: var(--charcoal); }
  .figure--researchers { fill: var(--lime-pale); }
  .motive-disc--organizers, .badge--organizers { fill: var(--charcoal); }
  .motive-disc--researchers, .badge--researchers { fill: var(--lime); }
  .badge { stroke: var(--paper); stroke-width: 4; }
  .badge-number {
    font-family: "Open Sans", sans-serif;
    font-size: 28px;
    fill: var(--paper);
    text-anchor: middle;
  }
  .motive-label {
    font-family: "Open Sans", sans-serif;
    font-size: 34px;
    fill: var(--ink);
    text-anchor: middle;
  }
  .icon-line { fill: none; stroke: var(--silver); stroke-linecap: round; }
  .icon-white-line { fill: none; stroke: var(--paper); stroke-linecap: round; stroke-linejoin: round; }
  .icon-white { fill: var(--paper); }
  .icon-bar { fill: var(--steel); }
  .icon-tile { fill: var(--steel); }
  .icon-tile--light { fill: #e6e6e6; }
  .icon-glyph {
    font-family: "Open Sans", sans-serif;
    font-weight: 600;
    fill: var(--paper);
    text-anchor: middle;
  }
</style>
</head>
<body>
<svg class="sheet" viewBox="0 0 1200 2603" xmlns="http://www.w3.org/2000/svg">
  <defs>
    <path id="badge-shape" d="M -30 30 L -21.5 -5.8 A 22 22 0 1 1 5.8 21.5 Z"/>
  </defs>

  <!-- Brand -->
  <g class="brand">
    <circle class="brand-dot" cx="232" cy="176" r="64"/>
    <text class="brand-name" x="322" y="240">Zelmora</text>
  </g>

  <!-- User groups -->
  <g class="group group--organizers">
    <rect class="figure--organizers" x="180" y="378" width="172" height="245" rx="34"
          role="img" aria-label="Illustration of a businessman in a suit and tie"/>
    <rect class="group-bar--organizers" x="170" y="626" width="305" height="58"/>
    <text class="group-label" x="290" y="667">Organizers</text>
  </g>
  <g class="group group--researchers">
    <rect class="figure--researchers" x="605" y="378" width="543" height="245" rx="34"
          role="img" aria-label="Illustration of three researchers, a woman, a man with glasses and a woman"/>
    <rect class="group-bar--researchers" x="579" y="626" width="569" height="58"/>
    <text class="group-label" x="864" y="667">Researchers</text>
  </g>

  <!-- Organizer motives -->
  <g class="motive">
    <circle class="motive-disc--organizers" cx="263" cy="910" r="122"/>
    <g class="icon-puzzle" role="img" aria-label="Puzzle pieces">
      <rect class="icon-tile" x="193" y="840" width="66" height="66" rx="6"/>
      <rect class="icon-tile--light" x="267" y="840" width="66" height="66" rx="6"/>
      <rect class="icon-tile" x="193" y="914" width="66" height="66" rx="6"/>
      <rect class="icon-tile" x="267" y="914" width="66" height="66" rx="6"/>
    </g>
    <use href="#badge-shape" class="badge badge--organizers" transform="translate(451 777)"/>
    <text class="badge-number" x="451" y="787">1</text>
    <text class="motive-label" x="290" y="1096">Solving business</text>
    <text class="motive-label" x="290" y="1140">problems</text>
  </g>
  <g class="motive">
    <circle class="motive-disc--organizers" cx="263" cy="1364" r="122"/>
    <g class="icon-recruit" role="img" aria-label="One candidate standing out among others">
      <rect class="icon-bar" x="193" y="1320" width="34" height="100" rx="10"/>
      <rect class="icon-white" x="246" y="1320" width="34" height="100" rx="10"/>
      <rect class="icon-bar" x="299" y="1320" width="34" height="100" rx="10"/>
      <line class="icon-white-line" x1="272" y1="1322" x2="288" y2="1278" stroke-width="9"/>
    </g>
    <use href="#badge-shape" class="badge badge--organizers" transform="translate(451 1231)"/>
    <text class="badge-number" x="451" y="1241">2</text>
    <text class="motive-label" x="290" y="1545">Recruiting</text>
  </g>
  <g class="motive">
    <circle class="motive-disc--organizers" cx="263" cy="1797" r="122"/>
    <g class="icon-chart">
      <rect class="icon-bar" x="203" y="1817" width="22" height="42"/>
      <rect class="icon-bar" x="233" y="1795" width="22" height="64"/>
      <rect class="icon-bar" x="263" y="1773" width="22" height="86"/>
      <rect class="icon-bar" x="293" y="1751" width="22" height="108"/>
      <path class="icon-white-line" d="M 193 1850 Q 275 1820 322 1742" stroke-width="7"/>
      <path class="icon-white" d="M 336 1718 L 309 1736 L 331 1751 Z"/>
    </g>
    <use href="#badge-shape" class="badge badge--organizers" transform="translate(451 1664)"/>
    <text class="badge-number" x="451" y="1674">3</text>
    <text class="motive-label" x="290" y="1957">Self-promotion</text>
  </g>
  <g class="motive">
    <circle class="motive-disc--organizers" cx="263" cy="2259" r="122"/>
    <g class="icon-clock">
      <circle class="icon-line" cx="263" cy="2259" r="88" stroke-width="6"/>
      <line class="icon-line" x1="263" y1="2259" x2="263" y2="2188" stroke-width="6"/>
      <line class="icon-line" x1="263" y1="2259" x2="228" y2="2209" stroke-width="5"/>
    </g>
    <use href="#badge-shape" class="badge badge--organizers" transform="translate(451 2126)"/>
    <text class="badge-number" x="451" y="2136">4</text>
    <text class="motive-label" x="290" y="2429">Doing Business with</text>
    <text class="motive-label" x="290" y="2473">the times.</text>
  </g>

  <!-- Researcher motives -->
  <g class="motive">
    <circle class="motive-disc--researchers" cx="858" cy="910" r="122"/>
    <g class="icon-medal">
      <path class="icon-white" d="M 828 940 L 808 1000 L 830 990 L 842 1010 L 852 955 Z"/>
      <path class="icon-white" d="M 888 940 L 908 1000 L 886 990 L 874 1010 L 864 955 Z"/>
      <circle cx="858" cy="900" r="52" fill="var(--lime)" stroke="var(--paper)" stroke-width="7"/>
      <text class="icon-glyph" x="858" y="927" font-size="74">$</text>
    </g>
    <use href="#badge-shape" class="badge badge--researchers" transform="translate(1033 777)"/>
    <text class="badge-number" x="1033" y="787">1</text>
    <text class="motive-label" x="862" y="1085">Earnings</text>
  </g>
  <g class="motive">
    <circle class="motive-disc--researchers" cx="858" cy="1364" r="122"/>
    <g class="icon-briefcase">
      <path class="icon-white-line" d="M 832 1330 V 1314 H 884 V 1330" stroke-width="9"/>
      <rect class="icon-white" x="788" y="1330" width="140" height="96" rx="8"/>
      <line x1="788" y1="1366" x2="928" y2="1366" stroke="var(--lime)" stroke-width="5"/>
      <rect x="848" y="1356" width="20" height="20" fill="var(--lime)"/>
    </g>
    <use href="#badge-shape" class="badge badge--researchers" transform="translate(1033 1231)"/>
    <text class="badge-number" x="1033" y="1241">2</text>
    <text class="motive-label" x="862" y="1537">Employability</text>
  </g>
  <g class="motive">
    <circle class="motive-disc--researchers" cx="858" cy="1797" r="122"/>
    <text class="icon-glyph" x="852" y="1862" font-size="180">?</text>
    <use href="#badge-shape" class="badge badge--researchers" transform="translate(1033 1664)"/>
    <text class="badge-number" x="1033" y="1674">3</text>
    <text class="motive-label" x="862" y="1946">Intelligent Leisure</text>
  </g>
  <g class="motive">
    <circle class="motive-disc--researchers" cx="858" cy="2259" r="122"/>
    <g class="icon-network">
      <g class="icon-white-line" stroke-width="6">
        <line x1="858" y1="2259" x2="858" y2="2185"/>
        <line x1="858" y1="2259" x2="922" y2="2222"/>
        <line x1="858" y1="2259" x2="922" y2="2296"/>
        <line x1="858" y1="2259" x2="858" y2="2333"/>
        <line x1="858" y1="2259" x2="794" y2="2296"/>
        <line x1="858" y1="2259" x2="794" y2="2222"/>
      </g>
      <circle class="icon-white" cx="858" cy="2259" r="14"/>
      <circle class="icon-white" cx="858" cy="2185" r="12"/>
      <circle class="icon-white" cx="922" cy="2222" r="12"/>
      <circle class="icon-white" cx="922" cy="2296" r="12"/>
      <circle class="icon-white" cx="858" cy="2333" r="12"/>
      <circle class="icon-white" cx="794" cy="2296" r="12"/>
      <circle class="icon-white" cx="794" cy="2222" r="12"/>
    </g>
    <use href="#badge-shape" class="badge badge--researchers" transform="translate(1033 2126)"/>
    <text class="badge-number" x="1033" y="2136">4</text>
    <text class="motive-label" x="862" y="2424">Communication</text>
  </g>
</svg>
</body>
</html>
```